Referral Club PostCard/ Index Card

I need to create an Index card for a Contractor Referral Club. I already did my own door hanger which I can show you. Cost is a factor because I'm just starting my company. You guys have already created my 2 logos when I did a previous logo project so I want to use those logos and colors to create a scheme double sided postcard for my referral club attached to our some examples of other ones I've seen. So, you can 1 of 3 different design/color schemes as a basis:
1) The Black background with Blue Shield
2). The Light Blue background with the white wave (Really like this and the black one)
3). My White background blue/black business card design.
So, 3 different design/color schemes to attack?

You can also look at my website for ideas

http://www.TheDwellingCounselor.example
Updates

I have a picture of the things I want to say on BOTH sides on the Index card/[Post card. Basically, there are two versions that can be created, one with the black background/blue logo motif or one with the white/blue background logo. I bought BOTH designs in my logo contest. Actually 1 is the front of the cards and the other is the back of my card. I'm looking for creativity to get these contractors to join this referral club so I can get more leads.

Need extra days to review

I have some new logos,, icons and pdfs to submit for consideration

Target Market(s)

Drawing Other Contractors into my Professional Referral Exchange Club

Industry/Entity Type

Public Insurance Adjusting

Font styles to use
Serif
Sans Serif
Other font styles liked:
• Love Zurich font but very few people have it..It is eye drawing!!

Colors
0054AA
0677BA
7BADD7
CADEEF
E8F1F8
0094D4
00A9DD
6FCCEA
C7EBF8
E9F6FB
EE7325
F08F49
F5BC92
FAE3D3
FDF4ED

Requirements
Must have
• My Blue or Black/White color scheme to stay consistent to what Ive already had done
Nice to have
• Something that jumps off to entice them to join that I haven't thought of.

```html
<!DOCTYPE html>
<html lang="en">
<head>
<meta charset="utf-8">
<title>The Dwelling Counselor – Referral Exchange Club Card</title>
<link href="https://fonts.googleapis.com/css2?family=Arimo:ital,wght@0,400;0,700;1,700&family=Tinos:wght@400;700&display=swap" rel="stylesheet">
<style>
  :root {
    --stage-grey: #939497;
    --stage-white: #ffffff;
    --brand-navy: #1f2a6b;
    --brand-blue: #0054aa;
    --brand-cyan: #0094d4;
    --brand-sky: #1a9ad6;
    --accent-orange: #ee7325;
    --alert-red: #e8202a;
    --ink: #111111;
    --ink-soft: #6d6e71;
    --paper: #ffffff;
    --paper-grey: #f2f2f2;
    --night: #1b1b1b;
    --text-light: #dedede;
    --store-grey: #8a8a8a;
  }
  * { box-sizing: border-box; margin: 0; padding: 0; }
  html, body { width: 984px; height: 1200px; overflow: hidden; background: var(--stage-white); }
  .stage {
    position: absolute; left: 0; top: 0; width: 950px; height: 1177px;
    background: var(--stage-grey);
  }
  .card {
    position: absolute; left: 177px; width: 602px; height: 399px;
    overflow: hidden;
    box-shadow: 4px 6px 10px rgba(0,0,0,.35);
    font-family: "Arimo", Arial, sans-serif;
  }
  .card-front { top: 150px; background: radial-gradient(ellipse at 45% 40%, #ffffff 40%, #ececec 100%); }
  .card-back { top: 622px; background: var(--night); }
  .card svg.backdrop { position: absolute; left: 0; top: 0; width: 602px; height: 399px; }
  .abs { position: absolute; }
  .center { left: 0; width: 602px; text-align: center; white-space: nowrap; }

  /* front */
  .brand-mark { left: 281px; top: 34px; width: 42px; height: 42px; background: var(--brand-blue); }
  .brand-name { top: 108px; font-family: "Tinos", "Times New Roman", serif; font-size: 21px; color: var(--brand-blue); letter-spacing: .5px; }
  .club-title { top: 163px; font-size: 23px; font-weight: 400; color: var(--ink); letter-spacing: .3px; }
  .services { top: 195px; font-size: 10.5px; line-height: 14px; font-weight: 700; font-style: italic; color: var(--accent-orange); }
  .join-pill {
    left: 76px; top: 234px; width: 442px; height: 28px; border-radius: 14px;
    background: linear-gradient(90deg, var(--brand-navy) 0%, #2a3f8a 40%, var(--brand-cyan) 100%);
    color: var(--paper); font-size: 12.5px; line-height: 28px; padding-left: 20px; white-space: nowrap;
  }
  .accolade { top: 272px; font-size: 12.5px; line-height: 15px; color: var(--ink-soft); }
  .coverage { top: 335px; font-size: 12.5px; color: #d6e4f2; }
  .phone-line { top: 354px; font-family: "Tinos", "Times New Roman", serif; font-size: 28px; color: var(--paper); }
  .rating { left: 460px; top: 24px; width: 142px; text-align: center; font-family: "Tinos", "Times New Roman", serif; color: var(--ink); line-height: 1; }
  .rating-grade { font-family: "Arimo", Arial, sans-serif; font-size: 18px; color: var(--alert-red); margin-bottom: 2px; }
  .rating-note { font-size: 9px; }
  .rating-source { font-size: 5.5px; color: var(--ink-soft); }
  .hero-photo { left: 443px; top: 88px; width: 159px; height: 196px; background: linear-gradient(160deg, #b7563f 0%, #e9e9e9 22%, #8d958d 55%, #6f7a6c 80%, #cfd1cd 100%); clip-path: polygon(45% 0, 100% 0, 100% 100%, 0 100%, 0 62%, 25% 30%, 45% 26%); }

  /* back */
  .back-photo { left: 0; top: 0; width: 602px; height: 330px; background: radial-gradient(ellipse at 50% 45%, #5a5a5a 0%, #2e2e2e 55%, #151515 100%); }
  .reasons-title { top: 38px; font-family: "Tinos", "Times New Roman", serif; font-size: 28px; line-height: 35px; font-weight: 400; color: var(--brand-sky); }
  .reason-list { list-style: none; }
  .reason { position: absolute; left: 40px; color: var(--text-light); font-size: 16.5px; line-height: 22px; }
  .reason-num {
    position: absolute; left: 0; top: -4px; width: 30px; height: 30px; border-radius: 50%;
    border: 1.5px solid transparent; border-left-color: var(--accent-orange); border-bottom-color: var(--accent-orange);
    color: var(--paper); font-size: 18px; text-align: center; line-height: 27px;
  }
  .reason-text { position: absolute; left: 44px; top: 0; white-space: nowrap; }
  .reason-text .store { font-size: 23px; font-weight: 700; color: var(--store-grey); margin-left: 12px; }
  .reason-text .or { margin: 0 12px; }
  .closing-offer { left: 63px; top: 354px; font-size: 18px; color: var(--ink); white-space: nowrap; }
  .seal { left: 472px; top: 262px; width: 104px; height: 104px; border-radius: 50%; background: linear-gradient(160deg, #2fa6e0, var(--brand-blue)); color: var(--paper); font-size: 11.5px; text-align: center; display: flex; align-items: center; justify-content: center; line-height: 15px; }
</style>
</head>
<body>
<div class="stage">

  <section class="card card-front">
    <div class="abs hero-photo" role="img" aria-label="Photo of a small house resting on stacks of banknotes"></div>

    <svg class="backdrop" viewBox="0 0 602 399" aria-hidden="true">
      <defs>
        <linearGradient id="frontWave" x1="0" x2="1" y1="0" y2="0">
          <stop offset="0" stop-color="#1a96d2"/>
          <stop offset=".55" stop-color="#1f5aa6"/>
          <stop offset="1" stop-color="#1f2a6b"/>
        </linearGradient>
      </defs>
      <path d="M0 270 Q300 330 602 264 L602 399 L0 399Z" fill="#111"/>
      <path d="M0 273 Q300 362 602 278 L602 399 L0 399Z" fill="url(#frontWave)"/>
    </svg>

    <div class="abs brand-mark"></div>
    <div class="abs center brand-name">THE DWELLING COUNSELOR</div>
    <h1 class="abs center club-title">REFERAL EXCHANGE CLUB</h1>
    <p class="abs center services">Public Adjusters &amp; Loss Consultants<br>Damage Assessors &amp; Certified Insurance Appraisers</p>
    <div class="abs join-pill">TO JOIN CLUB CLICK: pronet &nbsp;| Martin Okafor Hale | Exchange Club</div>
    <p class="abs center accolade">Best of the South 8x since 2010</p>
    <p class="abs center coverage">Servicing Florida, Georgia, Alabama and Mississippi</p>
    <p class="abs center phone-line">CALL 1-800-FIXCLAIM</p>

    <div class="abs rating">
      <div class="rating-grade">A+ Rating</div>
      <div class="rating-note">Highest Rating For<br>Public Insurance Adjusters</div>
      <div class="rating-source">(Source: IndustryReview)</div>
    </div>
  </section>

  <section class="card card-back">
    <div class="abs back-photo" role="img" aria-label="Dark blurred photo of a damaged home interior"></div>

    <svg class="backdrop" viewBox="0 0 602 399" aria-hidden="true">
      <defs>
        <linearGradient id="backWave" x1="0" x2="1" y1="0" y2="0">
          <stop offset="0" stop-color="#0094d4"/>
          <stop offset="1" stop-color="#1f5aa6"/>
        </linearGradient>
      </defs>
      <path d="M0 336 Q260 286 602 328 L602 399 L0 399Z" fill="url(#backWave)"/>
      <path d="M0 344 Q280 302 602 338 L602 399 L0 399Z" fill="#f2f2f2"/>
    </svg>

    <h2 class="abs center reasons-title">TOP FOUR REASONS<br>FOR JOINING THE CLUB</h2>

    <ol class="reason-list">
      <li class="reason" style="top:124px"><span class="reason-num">1</span><span class="reason-text">EXCLUSIVITY ONLY ONE PER INDUSTRY PER REGION</span></li>
      <li class="reason" style="top:173px"><span class="reason-num">2</span><span class="reason-text">GUARANTEED RETURN REFERRAL “ACCOUNTABILITY”</span></li>
      <li class="reason" style="top:214px"><span class="reason-num">3</span><span class="reason-text">$75 GIFT CERTIFICATE<span class="store">Freshway</span><span class="or">OR</span><span class="store" style="margin-left:0">Valuemart</span></span></li>
      <li class="reason" style="top:250px"><span class="reason-num" style="top:7px">4</span><span class="reason-text">TRUST YOUR CLIENT HAS THE BEST LOCAL<br>PUBLIC ADMINISTER</span></li>
    </ol>

    <p class="abs closing-offer">COMPLIMENTARY POLICY &amp; CLAIM REVIEW</p>
    <div class="abs seal">THE DWELLING<br>COUNSELOR</div>
  </section>

</div>
</body>
</html>
```